VelmoraMD is an aesthetics and wellness medical spa. I am looking for a modern site, not too glam, not too boring. Currently I have the coming soon page at velmoraMD.com. The green in the logo is the accent color. I need the site to be semi neutral. I don't want it to be too geared towards females because there are some consults that men also will participate in.

```html
<!DOCTYPE html>
<html lang="en">
<head>
<meta charset="utf-8">
<title>VelmoraMD — Aesthetics &amp; Wellness</title>
<link href="https://fonts.googleapis.com/css2?family=Montserrat:wght@300;400;500;600;700&display=swap" rel="stylesheet">
<style>
:root{
  --accent:#f26c56;
  --sage:#b8cec4;
  --sage-deep:#9fbbae;
  --mist:#eef3f0;
  --ink:#2e2e2e;
  --body:#555;
  --footer:#4b4b4d;
  --white:#fff;
}
*{box-sizing:border-box;margin:0;padding:0}
html,body{width:1200px;height:3971px;overflow:hidden}
body{position:relative;background:var(--white);font-family:'Montserrat',sans-serif;color:var(--ink)}
.backdrop{position:absolute;left:0;top:0;width:1200px;height:3971px}
.abs{position:absolute}
.brand{font-family:'Montserrat',sans-serif;font-weight:600;color:#3f4a46;display:flex;align-items:center;gap:10px}
.brand .dot{width:14px;height:14px;border-radius:50%;background:var(--sage-deep)}
.site-header .brand{left:62px;top:38px;font-size:34px}
.main-nav{left:349px;top:52px}
.main-nav a{position:absolute;white-space:nowrap;font-size:14px;font-weight:600;color:var(--ink);text-decoration:none}
.main-nav a.current{color:var(--sage-deep);font-weight:500}
.btn{display:flex;align-items:center;justify-content:center;background:var(--accent);color:var(--white);font-weight:600;font-size:16px;border-radius:30px;text-transform:uppercase;letter-spacing:.2px;white-space:nowrap}
.btn-provider{left:920px;top:37px;width:224px;height:49px;font-size:15px}
.hero-title{left:152px;top:294px;font-size:47px;font-weight:700;line-height:58px;color:#111;letter-spacing:.5px;white-space:nowrap}
.btn-start{left:157px;top:431px;width:146px;height:47px;font-size:15px}
.section-title{font-size:41px;font-weight:600;color:var(--ink);letter-spacing:.3px;white-space:nowrap}
.lorem{font-size:14px;font-weight:300;line-height:21px;color:var(--body);white-space:nowrap}
.about-title{left:154px;top:885px}
.about-text{left:151px;top:952px}
.btn-more{width:170px;height:49px;font-size:16px}
.photo-ring{border-radius:50%;border:13px solid var(--sage);background:var(--white);padding:10px}
.photo-ring .photo{width:100%;height:100%;border-radius:50%}
.about-photo{left:617px;top:868px;width:432px;height:432px}
.about-photo .photo{background:radial-gradient(circle at 40% 40%,#e9eef0,#9fb3c2 55%,#2f4a6e)}
.services-title{left:0;width:1200px;top:1398px;text-align:center}
.services-intro{left:0;width:1200px;top:1464px;text-align:center;font-size:17px;font-weight:300;line-height:24px;color:var(--body)}
.service{width:262px;height:262px;border-radius:50%;border:6px solid var(--sage-deep);background:var(--white);padding:4px}
.service .photo{width:100%;height:100%;border-radius:50%;display:flex;align-items:center;justify-content:center;color:var(--white);font-weight:700;font-size:21px;text-shadow:0 1px 3px rgba(0,0,0,.35);white-space:nowrap}
.s1 .photo{background:linear-gradient(135deg,#d8d6d3,#8e7a6c)}
.s2 .photo{background:linear-gradient(135deg,#5b5552,#c3a99a)}
.s3 .photo{background:linear-gradient(135deg,#c7ccd3,#a98f84)}
.s4 .photo{background:linear-gradient(135deg,#a9c2dd,#e6d1c4)}
.s5 .photo{background:linear-gradient(135deg,#8a9a8e,#ece7e2)}
.s6 .photo{background:linear-gradient(135deg,#6f6a8a,#3d6f78)}
.journey-text{left:111px;top:2370px;font-size:31px;font-weight:600;line-height:38px;color:var(--white);letter-spacing:.3px;white-space:nowrap}
.journey-photo{left:630px;top:2195px;width:440px;height:490px;background:linear-gradient(135deg,#c9d7d0 0%,#dccbbd 100%)}
.community-title{left:0;width:1200px;top:2836px;text-align:center;font-size:32px;font-weight:600;line-height:38px;color:var(--ink)}
.signup{left:188px;top:2962px;width:822px;height:42px}
.field{position:absolute;top:0;height:42px;border-radius:21px;background:#eef0ef;font-size:12px;font-weight:500;color:#444;padding-left:20px;display:flex;align-items:center}
.signup .btn{position:absolute;top:0;left:625px;width:197px;height:42px;font-size:16px}
.latest-title{left:154px;top:3135px;line-height:46px}
.latest-text{left:151px;top:3241px}
.latest-photo{left:617px;top:3112px;width:432px;height:432px}
.latest-photo .photo{background:radial-gradient(circle at 45% 50%,#f0d9cb,#e4c4b1 45%,#f4f2f0 75%)}
.site-footer .brand{left:0;width:1200px;justify-content:center;top:3752px;font-size:40px;color:var(--white)}
.site-footer .brand .dot{background:var(--sage)}
.footer-nav{left:0;width:1200px;top:3842px;display:flex;justify-content:center;gap:40px;font-size:14px;font-weight:600;color:var(--white)}
.footer-legal{left:0;width:1200px;top:3895px;display:flex;justify-content:center;gap:34px;font-size:13.5px;font-weight:400;color:#e6e6e6}
</style>
</head>
<body>
<svg class="backdrop" viewBox="0 0 1200 3971" aria-hidden="true">
  <path d="M1200 740 C950 760 870 1000 720 1150 C570 1300 300 1330 0 1440 L0 2250 L1200 2250 Z" fill="var(--mist)"/>
  <path d="M0 2255 C300 2160 900 2150 1200 2240 L1200 2650 C900 2730 300 2735 0 2620 Z" fill="var(--sage)"/>
  <path d="M0 2240 C300 2145 900 2135 1200 2225" fill="none" stroke="var(--white)" stroke-width="4"/>
  <path d="M0 3740 C350 3640 850 3640 1200 3760 L1200 3971 L0 3971 Z" fill="var(--footer)"/>
  <path d="M0 3720 C350 3610 850 3610 1200 3745 L1200 3770 C850 3640 350 3640 0 3745 Z" fill="var(--sage)"/>
</svg>

<header class="site-header">
  <div class="brand abs"><span class="dot"></span>VelmoraMD</div>
  <nav class="main-nav abs">
    <a class="current" style="left:0">HOME</a>
    <a style="left:87px">ABOUT</a>
    <a style="left:183px">SERVICES</a>
    <a style="left:297px">TESTIMONIALS</a>
    <a style="left:450px">CONTACT</a>
  </nav>
  <a class="btn btn-provider abs">Become a provider</a>
</header>

<section class="hero">
  <svg class="abs" style="left:0;top:116px" width="1200" height="660" viewBox="0 0 1200 660">
    <defs>
      <linearGradient id="heroTone" x1="0" y1="0" x2="1" y2="1">
        <stop offset="0" stop-color="#b8a89a"/><stop offset=".5" stop-color="#a9c2c8"/><stop offset="1" stop-color="#c99a78"/>
      </linearGradient>
    </defs>
    <path role="img" aria-label="Woman relaxing in a spa whirlpool" d="M0 0 H1200 V500 Q600 640 0 530 Z" fill="url(#heroTone)"/>
    <path d="M0 530 Q600 640 1200 500 L1200 530 Q600 680 0 570 Z" fill="var(--sage)"/>
  </svg>
  <h1 class="hero-title abs">LOOK AND FEEL<br>YOUR BEST</h1>
  <a class="btn btn-start abs">Start now</a>
</section>

<section class="about">
  <h2 class="section-title about-title abs">ABOUT US</h2>
  <p class="lorem about-text abs">Lorem ipsum dolor sit amet, consectetur adipiscing elit,<br>sed do eiusmod tempor incididunt ut labore et dolore<br>magna aliqua. Quis ipsum suspendisse ultrices gravida.<br>Risus commodo viverra maecenas accumsan lacus vel<br>facilisis. Lorem ipsum dolor sit amet, consectetur adip<br>iscing elit, sed do eiusmod tempor incididunt ut labore<br>et dolore magna aliqua. Quis ipsum suspendisse ultr<br>ices gravida. Risus commodo viverra maecenas<br>accumsan lacus vel facilisis.</p>
  <a class="btn btn-more abs" style="left:154px;top:1167px">Read more</a>
  <div class="photo-ring about-photo abs"><div class="photo" role="img" aria-label="Practitioner giving a client a facial injection"></div></div>
</section>

<section class="services">
  <h2 class="section-title services-title abs">SERVICES</h2>
  <p class="services-intro abs">Lorem ipsum dolor sit amet, consectetur adipiscing elit, sed do eiusmod<br>tempor incididunt ut labore et dolore magna aliqua ipsum susp</p>
  <div class="service s1 abs" style="left:173px;top:1539px"><div class="photo" role="img" aria-label="Man receiving a botox treatment">Botox Parties</div></div>
  <div class="service s2 abs" style="left:470px;top:1539px"><div class="photo" role="img" aria-label="Woman receiving dermal filler">Dermal Fillers</div></div>
  <div class="service s3 abs" style="left:769px;top:1539px"><div class="photo" role="img" aria-label="IV drip being placed in an arm">IV Therapy</div></div>
  <div class="service s4 abs" style="left:173px;top:1832px"><div class="photo" role="img" aria-label="Client during a treatment">ED</div></div>
  <div class="service s5 abs" style="left:470px;top:1832px"><div class="photo" role="img" aria-label="Woman in a clinic consultation">BHRT</div></div>
  <div class="service s6 abs" style="left:769px;top:1832px"><div class="photo" role="img" aria-label="Microscopic cell illustration">Peptides</div></div>
</section>

<section class="journey">
  <p class="journey-text abs">START OR CONTINUE YOUR<br>AESTHETICS AND WELLNESS<br>JOURNEY HERE.</p>
  <div class="journey-photo abs" role="img" aria-label="Portrait of a woman with facial contour lines"></div>
</section>

<section class="community">
  <h2 class="community-title abs">A MOTIVATION PLATFORM &nbsp;- WE ARE MORE<br>THAN A CLINIC, JOIN OUR COMMUNITY.</h2>
  <form class="signup abs">
    <div class="field" style="left:0;width:198px">Name:</div>
    <div class="field" style="left:207px;width:197px">Email:</div>
    <div class="field" style="left:418px;width:197px">Phone:</div>
    <span class="btn">Sign up</span>
  </form>
</section>

<section class="latest">
  <h2 class="section-title latest-title abs">THE LATEST<br>PROCEDURES</h2>
  <p class="lorem latest-text abs">Lorem ipsum dolor sit amet, consectetur adipiscing elit,<br>sed do eiusmod tempor incididunt ut labore et dolore<br>magna aliqua. Quis ipsum suspendisse ultrices gravida.<br>Risus commodo viverra maecenas accumsan lacus vel<br>facilisis. Lorem ipsum dolor sit amet, consectetur adip<br>iscing elit, sed do eiusmod tempor incididunt ut labore<br>et dolore magna aliqua</p>
  <a class="btn btn-more abs" style="left:154px;top:3414px">Read more</a>
  <div class="photo-ring latest-photo abs"><div class="photo" role="img" aria-label="Relaxed client receiving a cosmetic injection"></div></div>
</section>

<footer class="site-footer">
  <div class="brand abs"><span class="dot"></span>VelmoraMD</div>
  <nav class="footer-nav abs"><span>HOME</span><span>ABOUT</span><span>SERVICES</span><span>TESTIMONIALS</span><span>CONTACT</span></nav>
  <div class="footer-legal abs"><span>© 2022 VelmoraMD</span><span>Terms of Use</span><span>Membership Terms &amp; Conditions</span><span>Privacy Policy</span></div>
</footer>
</body>
</html>
```